BrightLoop (1 page) homepage re-design

Our homepage needs a face-lift! We need our homepage on our website re-designed with a fresh and current look and feel. We have all the details, colour codes and a rough wireframe ready, but need a talented designer to put some personality into our ideas.

What we do: BrightLoop is a digital marketing agency with offices in Australia (Sydney) and South Africa (Cape Town). We specialise in SEO, PPC (otherwise known as Zentro PayLine or SEM), content marketing and Zentro Tallyboard. We use these tools to help our clients realise their business dreams.

VISUAL

Style / theme of the design:
Clean, simplistic, fun, flow.

Websites we draw inspiration from:
This is the theme we want to use to build the website
http://demo.vormalayouts.example/vl/?theme=Pebbled
Inspiration:
https://www.ondrapromo.example/
https://www.nelvagrowth.example.au/
https://quimbel.example.au/
https://torvin.layout-works.example/forum/

What we like about the site:
Clean, simple design, good use of white space. The subtle changing background colours, strong contrast with text. Not too busy or distracting.

What we don’t want: Too many different colours.

Target Market(s)

Our target audience: Marketing Managers of small to medium size businesses in Australia.

Industry/Entity Type

Marketing

Number of Pages Required

1 page

Font styles to use
Sans Serif

Requirements
Must have
• Elements to be added on homepage in order and as seen in attachments:
• - Section 1: Video with team as image and a play button add the heading: We help smart marketing managers achieve their KPIs [line break] and reduce their digital marketing overwhelm.
• - Section 2: Solutions section with the 6 solutions displayed in a row.
• - Section 3: Register Free Webinar with video
• - Section 4: Please add 3 case studies (as seen in attached docs there is only 1 but please add 3 below each other)
• - Section 5: Clients. Please add all client logo’s (black and white)
• - Section 6: Our Blog (as seen attached)
• - Section 7: Conferences Attended (please add the title and a paragraph of lorem Ipsom below) and then please add all conference logo’s attached below.
• - Section 8: In The Media (please add all logo’s titled media) white background
• - Section 9: Footer (dark grey footer) add our Zentro honoured affiliate logo here please
• - Section10: Footer - include:
• - Social logos (WorkMesh, Blipster, Pallwall, ReelDrop, Zentro Hub)
• - Navigation
• - Contact details (name, address, phone number, email)
• Colour codes:
• We want to use light greys, white and charcoal grey for the backgrounds with a pop of our green colour to bring out our branding and all CTA’s to be orange, colour codes below:
• Light grey: #F2F2F2
• Charcoal grey: #161616
• Green: #428E29
• CTA’s: #de7532
• PLEASE NOTE: Please see attached pdf titled: homepagecopybrief.pdf for all the titles and statistics that need to go on the homepage
Should not have
• Too much colour, icons should not be different colours

```html
<!DOCTYPE html>
<html lang="en">
<head>
<meta charset="utf-8">
<title>BrightLoop — Digital Marketing</title>
<link rel="stylesheet" href="https://fonts.googleapis.com/css2?family=Poppins:wght@400;500;700;800&display=swap">
<style>
  :root {
    --page-bg: #ffffff;
    --light-grey: #f2f2f2;
    --charcoal: #161616;
    --header-grey: #3a3a3a;
    --green: #428e29;
    --cta: #de7532;
    --heading: #161616;
    --title-grey: #555555;
    --body-grey: #707070;
    --white: #ffffff;
  }
  * { box-sizing: border-box; margin: 0; padding: 0; }
  html, body { width: 1200px; height: 1200px; overflow: hidden; background: var(--page-bg); }
  body { font-family: "Poppins", sans-serif; position: relative; }

  .site-header {
    position: absolute; left: 150px; top: 0; width: 900px; height: 56px;
    background: linear-gradient(180deg, #2e2e2e, #474747);
    border-bottom: 1px solid #9a9a9a;
  }
  .brand { position: absolute; left: 112px; top: 14px; display: flex; align-items: center; gap: 8px; }
  .brand-square { width: 20px; height: 20px; background: var(--green); }
  .brand-name { color: var(--white); font-size: 20px; font-weight: 500; letter-spacing: 2px; line-height: 1; }
  .header-address { position: absolute; left: 448px; top: 20px; color: var(--white); font-size: 10.5px; }
  .header-phone { position: absolute; left: 657px; top: 18px; color: var(--cta); font-size: 13.5px; }
  .menu-toggle { position: absolute; left: 760px; top: 13px; color: var(--white); font-size: 8px; font-weight: 700; }
  .menu-toggle span { display: block; width: 26px; height: 2px; background: var(--white); margin-top: 3px; }
  .menu-toggle span:first-of-type { margin-top: 5px; }

  .hero {
    position: absolute; left: 150px; top: 56px; width: 900px; height: 540px;
    background: radial-gradient(ellipse at 55% 55%, #6c6660 0%, #4a4644 45%, #2c2b2b 100%);
  }
  .hero-title { position: absolute; left: 113px; top: 281px; color: var(--white); font-size: 21px; line-height: 42px; font-weight: 400; letter-spacing: 0.3px; }
  .hero-title strong { font-weight: 800; }
  .hero-title .amp { color: var(--green); font-weight: 700; }
  .hero-cta {
    position: absolute; left: 113px; top: 371px; width: 208px; height: 49px;
    background: var(--cta); color: var(--white); font-size: 16px; font-weight: 700;
    letter-spacing: 0.5px; display: flex; align-items: center; justify-content: center;
  }

  .solutions { position: absolute; left: 150px; top: 613px; width: 900px; height: 543px; background: var(--light-grey); }
  .solutions-title { position: absolute; left: 0; width: 900px; top: 40px; text-align: center; font-size: 29px; font-weight: 700; color: var(--heading); }
  .solutions-intro { position: absolute; left: 0; width: 900px; top: 100px; text-align: center; font-size: 14px; line-height: 24px; color: var(--title-grey); letter-spacing: 0.4px; }
  .solution { position: absolute; width: 215px; }
  .solution h3 { font-size: 17px; font-weight: 500; color: var(--title-grey); line-height: 24px; letter-spacing: 0.4px; }
  .solution h3.is-active { color: var(--cta); }
  .solution p { color: var(--body-grey); letter-spacing: 0.3px; }
  .row-one p { font-size: 10.5px; line-height: 17px; margin-top: 9px; }
  .row-two p { font-size: 14px; line-height: 20px; margin-top: 8px; }

  .next-panel { position: absolute; left: 150px; top: 1177px; width: 900px; height: 23px; background: var(--light-grey); }
</style>
</head>
<body>
  <header class="site-header">
    <div class="brand"><div class="brand-square"></div><div class="brand-name">BrightLoop</div></div>
    <div class="header-address">42 Harlow Lane, Millers Point, Sydney</div>
    <div class="header-phone">1300 472 615</div>
    <div class="menu-toggle">MENU<span></span><span></span><span></span></div>
  </header>

  <section class="hero" role="img" aria-label="Team photo of nine smiling agency staff standing together against a dark wall">
    <h1 class="hero-title"><strong>We help smart marketing managers achieve</strong> their KPIs<br><span class="amp">&amp;</span> reduce their digital marketing overwhelm.</h1>
    <div class="hero-cta">FIND OUT MORE</div>
  </section>

  <section class="solutions">
    <h2 class="solutions-title">Solutions</h2>
    <p class="solutions-intro">We turn SEO and PPC campaigns into refined lead generating machines<br>with refreshing transparency</p>

    <div class="solution row-one" style="left:112px; top:208px;">
      <h3>Grow Revenue</h3>
      <p>Lorem ipsum dolor sit amet, consectetur adipisicing elit, sed do eiusmod tempor incididunt ut labore et dolore magna aliqua. Ut enim ad</p>
    </div>
    <div class="solution row-one" style="left:345px; top:208px;">
      <h3 class="is-active">Convert Leads</h3>
      <p>Lorem ipsum dolor sit amet, consectetur adipisicing elit, sed do eiusmod tempor incididunt ut labore et dolore magna aliqua. Ut enim ad</p>
    </div>
    <div class="solution row-one" style="left:578px; top:208px;">
      <h3>Incresse Brand<br>Awareness</h3>
      <p style="margin-top:3px;">Lorem ipsum dolor sit amet, consectetur adipisicing elit, sed do eiusmod tempor incididunt ut labore</p>
    </div>

    <div class="solution row-two" style="left:112px; top:360px;">
      <h3>Data/ KPI’s</h3>
      <p>Lorem ipsum dolor sit amet, consectetur adipisicing elit, sed do eiusmod tempor incididunt ut labore et dolore</p>
    </div>
    <div class="solution row-two" style="left:345px; top:360px;">
      <h3>Incrasese engagement</h3>
      <p>Lorem ipsum dolor sit amet, consectetur adipisicing elit, sed do eiusmod tempor incididunt ut labore et dolore</p>
    </div>
    <div class="solution row-two" style="left:578px; top:360px;">
      <h3>Marketing Strategy<br>budgeting</h3>
      <p style="margin-top:4px;">Lorem ipsum dolor sit amet, consectetur adipisicing elit, sed do eiusmod tempor</p>
    </div>
  </section>

  <div class="next-panel"></div>
</body>
</html>
```